Eye Grabbing - Travel Consultant Business Card

I need a business card that stands out. Vertical instead of horizontal, rounded edges, would love to use the same layout item for magnets. I have uploaded my current logo and tag line. Would love a cool eye-grabbing image for the front side. Can be something different than what you see on my website as I am looking to rebrand as a Leisure, Luxury & Adventure Specialist.

Target Market(s)

Leisure and Luxury Travel

Industry/Entity Type

Travel Agent

Contact Information for Business Card

Company Name - oMbrella Voyages; Name - Priya Halworth; Title - Travel Consultant; Website - www.ombrellavoyages.com ; Phone: 318-662-0954 Email priya@ombrellavoyages.com and my facebook, twitter, and Instagram handles

Font styles to use
Serif

Colors

Designer to choose colors to be used in the design.

Requirements
Must have
• my tag line of -- Dream Explore Discover
Nice to have

```html
<!DOCTYPE html>
<html lang="en">
<head>
<meta charset="utf-8">
<title>oMbrella Voyages – Business Card</title>
<link rel="stylesheet" href="https://fonts.googleapis.com/css2?family=Mulish:wght@400;600;800&family=Montserrat:wght@500;800&display=swap">
<style>
  :root {
    --page: #3a3a3a;
    --card-white: #f4f4f4;
    --card-dark: #1b1b1b;
    --teal: #2bb3b1;
    --teal-light: #5fc8c4;
    --blue: #3f6fb0;
    --lime: #d8e24a;
    --green: #7cc142;
    --ink: #1e1e1e;
  }
  * { box-sizing: border-box; margin: 0; padding: 0; }
  html, body { width: 1200px; height: 1021px; overflow: hidden; }
  body {
    background: var(--page);
    font-family: "Mulish", sans-serif;
    position: relative;
  }
  .card {
    position: absolute;
    top: 195px;
    width: 360px;
    height: 630px;
    border-radius: 26px;
    overflow: hidden;
  }

  /* Front card */
  .card--front {
    left: 210px;
    background: var(--card-white);
    text-align: center;
  }
  .brand {
    position: absolute;
    top: 110px;
    left: 0; right: 0;
    display: flex;
    flex-direction: column;
    align-items: center;
    gap: 18px;
  }
  .brand__dot {
    width: 92px; height: 92px;
    border-radius: 50%;
    background: var(--teal);
  }
  .brand__name {
    font-family: "Montserrat", sans-serif;
    font-weight: 800;
    font-size: 30px;
    letter-spacing: -0.5px;
    color: var(--teal);
  }
  .contact {
    position: absolute;
    top: 330px;
    left: 0; right: 0;
  }
  .contact__name {
    font-weight: 800;
    font-size: 22px;
    color: var(--teal);
    letter-spacing: 0.3px;
  }
  .contact__title {
    font-size: 18px;
    color: var(--ink);
    margin-top: 2px;
  }
  .contact__icons {
    display: flex;
    justify-content: center;
    gap: 12px;
    margin: 14px 0 8px;
  }
  .contact__icons svg { width: 16px; height: 16px; }
  .contact__line {
    font-size: 17px;
    color: var(--ink);
    line-height: 1.55;
  }
  .contact__rule {
    width: 48px;
    height: 3px;
    background: var(--ink);
    margin: 34px auto 0;
  }

  /* Back card */
  .card--back {
    left: 630px;
    background: var(--card-dark);
  }
  .back__top {
    position: absolute;
    top: 40px;
    left: 0; right: 0;
    text-align: center;
  }
  .tagline {
    font-family: "Montserrat", sans-serif;
    font-weight: 500;
    font-size: 16px;
    letter-spacing: 3px;
    background: linear-gradient(90deg, var(--lime), var(--green), var(--blue));
    -webkit-background-clip: text;
    background-clip: text;
    color: transparent;
  }
  .social {
    display: flex;
    justify-content: center;
    align-items: center;
    gap: 8px;
    margin-top: 26px;
    font-size: 15px;
    letter-spacing: 1px;
    color: #e8e8e8;
  }
  .social__mark {
    width: 14px; height: 14px;
    border-radius: 3px;
    background: var(--green);
  }
  .back__art {
    position: absolute;
    left: 0; right: 0; bottom: 0;
    height: 430px;
    background:
      radial-gradient(circle at 50% 62%, #1b1b1b 0 140px, transparent 141px),
      linear-gradient(160deg, var(--teal-light) 0%, var(--teal) 55%, var(--blue) 100%);
  }
</style>
</head>
<body>
  <section class="card card--front">
    <div class="brand">
      <div class="brand__dot"></div>
      <div class="brand__name">oMbrella Voyages</div>
    </div>
    <div class="contact">
      <div class="contact__name">PRIYA HALWORTH</div>
      <div class="contact__title">Travel Consultant</div>
      <div class="contact__icons">
        <svg viewBox="0 0 16 16" aria-label="phone"><path d="M4 1l3 3-1.5 2a9 9 0 0 0 4.5 4.5L12 9l3 3-2 3C7 15 1 9 1 3z" fill="#2bb3b1"/></svg>
        <svg viewBox="0 0 16 16" aria-label="email"><rect x="1.5" y="3.5" width="13" height="9" fill="none" stroke="#2bb3b1" stroke-width="1.5"/><path d="M1.5 3.5l6.5 5 6.5-5" fill="none" stroke="#2bb3b1" stroke-width="1.5"/></svg>
        <svg viewBox="0 0 16 16" aria-label="website"><circle cx="8" cy="8" r="6.5" fill="none" stroke="#2bb3b1" stroke-width="1.5"/><path d="M1.5 8h13M8 1.5c-3 3.5-3 9.5 0 13M8 1.5c3 3.5 3 9.5 0 13" fill="none" stroke="#2bb3b1" stroke-width="1.2"/></svg>
      </div>
      <div class="contact__line">318-662-0954</div>
      <div class="contact__line">priya@ombrellavoyages.com</div>
      <div class="contact__line">www.ombrellavoyages.com</div>
      <div class="contact__rule"></div>
    </div>
  </section>

  <section class="card card--back">
    <div class="back__top">
      <div class="tagline">Dream. Explore. Discover</div>
      <div class="social">
        <span class="social__mark"></span>
        <span>OMBRELLAVOYAGES</span>
      </div>
    </div>
    <div class="back__art" role="img" aria-label="Illustration of an airplane trailing a curve over a cruise ship and sunset circle, in teal on black"></div>
  </section>
</body>
</html>
```